Business cards / Stationery
Stationery
Professional
Tomas Belcourt
MPT, CST, LMT
1400 North Pelham Road
Fairhaven, Oregon 97321
tomas.belcourt@merrowcareclinic.com
www.merrowcareclinic.com

```html
<!DOCTYPE html>
<html lang="en">
<head>
<meta charset="utf-8">
<title>Merrow Care – Business Card</title>
<link rel="stylesheet" href="https://fonts.googleapis.com/css2?family=Open+Sans:wght@400;600;700&display=swap">
<style>
  :root {
    --backdrop: #e9ecef;
    --card: #ffffff;
    --card-edge: #d9dde1;
    --brand-blue: #2b9fd8;
    --brand-blue-light: #6fbfe6;
    --ink: #2f2f2f;
    --ink-soft: #444444;
  }
  * { margin: 0; padding: 0; box-sizing: border-box; }
  html, body {
    width: 1200px;
    height: 901px;
    overflow: hidden;
    background: var(--backdrop);
    font-family: "Open Sans", Arial, sans-serif;
  }
  .business-card {
    position: absolute;
    left: 110px;
    top: 168px;
    width: 980px;
    height: 564px;
    background: var(--card);
    border: 1px solid var(--card-edge);
    box-shadow: 0 12px 36px rgba(0, 0, 0, 0.12);
  }
  .accent-bar {
    position: absolute;
    left: 0;
    top: 269px;
    width: 10px;
    height: 209px;
    background: var(--brand-blue);
  }
  .person-name {
    position: absolute;
    left: 90px;
    top: 124px;
    font-size: 42px;
    line-height: 50px;
    font-weight: 600;
    color: var(--brand-blue);
    white-space: nowrap;
  }
  .credentials {
    position: absolute;
    left: 90px;
    top: 188px;
    font-size: 26px;
    line-height: 34px;
    font-weight: 700;
    color: var(--ink);
    white-space: nowrap;
  }
  .contact-block {
    position: absolute;
    left: 90px;
    top: 258px;
    font-size: 22px;
    line-height: 33px;
    color: var(--ink-soft);
    white-space: nowrap;
  }
  .contact-block .gap { height: 30px; }
  .brand {
    position: absolute;
    left: 515px;
    top: 130px;
    width: 420px;
    text-align: center;
  }
  .brand-mark {
    display: block;
    margin: 0 auto 16px;
  }
  .brand-name {
    font-size: 50px;
    font-weight: 700;
    color: var(--brand-blue);
    line-height: 1;
    white-space: nowrap;
  }
  .brand-tagline {
    margin-top: 6px;
    font-size: 19px;
    font-weight: 400;
    color: var(--brand-blue-light);
    letter-spacing: 2.5px;
    text-transform: uppercase;
    white-space: nowrap;
  }
</style>
</head>
<body>
  <div class="business-card">
    <div class="accent-bar"></div>

    <h1 class="person-name">Tomas Belcourt</h1>
    <p class="credentials">MPT, CST, LMT</p>

    <div class="contact-block">
      <p>1400 North Pelham Road</p>
      <p>Fairhaven, Oregon 97321</p>
      <div class="gap"></div>
      <p>(541) 555-0142</p>
      <p>(541) 555-0187</p>
      <p>tomas.belcourt@merrowcareclinic.com</p>
      <p>www.merrowcareclinic.com</p>
    </div>

    <div class="brand">
      <svg class="brand-mark" width="170" height="170" viewBox="0 0 170 170" aria-hidden="true">
        <circle cx="85" cy="85" r="84" fill="var(--brand-blue)"/>
      </svg>
      <div class="brand-name">MERROW CARE</div>
      <div class="brand-tagline">Restorative Body Therapy</div>
    </div>
  </div>
</body>
</html>
```